Business Card Design Project - Brantwell Media

We need a new business card that fits with our new logo. We are a social media agency and consultancy operating in China. We want a fresh and strong business card. Our cards need to be two-sided as we have both English and Chinese language names and addresses on the card, but as with our current business card this does not need to be a mirror-image. Our thoughts go out to a white card on the front where the logo/name is and then using the logo colours for different coloured back-grounds. i.e that the back of the biz card works with the four different colours in the logo.

Attached is the new logo, and also a copy of our old business cards.

Target Market(s)

CEO's, CMO's. media and advertising professionals

Industry/Entity Type

Business

Requirements
Must have
• inclusion of both Chinese and English language
Nice to have
• four different colored versions of the back of the biz card. Our logo has four colors and each of these colors we would like to have a version of.

```html
<!DOCTYPE html>
<html lang="en">
<head>
<meta charset="utf-8">
<title>Brantwell Media – Business Card</title>
<link rel="stylesheet" href="https://fonts.googleapis.com/css2?family=Aldrich&family=Cinzel&family=Noto+Sans+SC:wght@400;500&display=swap">
<style>
  :root {
    --bg: #d6d6d8;
    --card: #ffffff;
    --ink: #1c1c1c;
    --purple: #5b2a86;
    --pink: #e5157e;
    --green: #7dbb2f;
    --orange: #ee5524;
    --orange-soft: #f8a27f;
    --label: #3a3a3a;
  }
  * { margin: 0; padding: 0; box-sizing: border-box; }
  html, body { width: 1200px; height: 765px; overflow: hidden; }
  body {
    position: relative;
    background: var(--bg);
    font-family: "Aldrich", sans-serif;
    color: var(--ink);
  }
  .card {
    position: absolute;
    top: 302px;
    width: 574px;
    height: 343px;
    border-radius: 42px;
    background: var(--card);
    overflow: hidden;
  }
  .card--front { left: 16px; }
  .card--back { left: 604px; }

  /* Front */
  .brand {
    position: absolute;
    left: 0; right: 0; top: 118px;
    display: flex; justify-content: center; align-items: center; gap: 12px;
  }
  .brand__mark { width: 14px; height: 14px; background: var(--purple); }
  .brand__name { font-size: 44px; letter-spacing: 1px; color: var(--ink); line-height: 1; }
  .web {
    position: absolute;
    left: 0; right: 0; top: 270px;
    text-align: center;
    font-size: 13px;
    letter-spacing: 9px;
  }
  .web .w1 { color: var(--green); }
  .web .w2 { color: var(--purple); }
  .web .w3 { color: var(--pink); }
  .web .w4 { color: var(--orange); }

  /* Back */
  .tile { position: absolute; }
  .tile--purple { left: 0; top: 0; width: 398px; height: 173px; background: var(--purple); }
  .tile--pink { left: 402px; top: 0; width: 172px; height: 173px; background: var(--pink); }
  .tile--green { left: 0; top: 177px; width: 398px; height: 64px; background: var(--green); }
  .tile--orange { left: 402px; top: 177px; width: 172px; height: 64px; background: var(--orange);
    display: flex; align-items: center; justify-content: center; }
  .tile--orange .brand__name { font-size: 21px; color: var(--orange-soft); }

  .person { position: absolute; left: 46px; top: 104px; color: #fff; }
  .person__name { font-size: 36px; line-height: 1; letter-spacing: 0.5px; }
  .person__role { font-size: 14px; margin-top: 6px; letter-spacing: 0.5px; }

  .address { position: absolute; left: 46px; top: 9px; color: #fff; font-size: 7.5px; line-height: 12px; }
  .address .cn { font-family: "Noto Sans SC", sans-serif; }
  .cn-name { position: absolute; left: 275px; top: 40px; color: #fff; font-family: "Noto Sans SC", sans-serif; font-size: 12px; font-weight: 500; }
  .cn-name small { font-size: 7px; margin-left: 4px; }

  .contacts {
    position: absolute; left: 46px; right: 36px; top: 251px;
    display: flex; justify-content: space-between;
    font-size: 11.5px; color: var(--ink); letter-spacing: 0.3px;
  }

  .side-label {
    position: absolute; top: 686px;
    font-family: "Cinzel", serif; font-size: 14px; letter-spacing: 3px; color: var(--label);
  }
  .side-label--front { left: 66px; }
  .side-label--back { left: 659px; }
</style>
</head>
<body>
  <section class="card card--front" aria-label="Card front">
    <div class="brand">
      <span class="brand__name">brantwell media</span>
      <span class="brand__mark" aria-hidden="true"></span>
    </div>
    <p class="web"><span class="w1">www.</span><span class="w2">brantwell</span><span class="w3">china</span><span class="w4">.com</span></p>
  </section>

  <section class="card card--back" aria-label="Card back">
    <div class="tile tile--purple">
      <div class="person">
        <p class="person__name">Daniel Harrow</p>
        <p class="person__role">Managing Director</p>
      </div>
    </div>
    <div class="tile tile--pink"></div>
    <div class="tile tile--green">
      <div class="address">
        <p class="cn">布朗维尔咨询（北京）有限公司</p>
        <p class="cn">北京市东城区东四北大街朗园商务中心C118（100010）</p>
        <p>Suite C118, Lang Yuan Business Plaza</p>
        <p>Dongsi North Rd Dongcheng District, Beijing 100010</p>
      </div>
      <p class="cn-name">韩德伦<small>董事总经理</small></p>
    </div>
    <div class="tile tile--orange">
      <span class="brand__name">brantwell media</span>
    </div>
    <div class="contacts">
      <span>email: daniel@harrowmail.com</span>
      <span>call: danbeijing</span>
      <span>mobile: +86 13800451276</span>
    </div>
  </section>

  <p class="side-label side-label--front">FRONT</p>
  <p class="side-label side-label--back">BACK</p>
</body>
</html>
```